Financial Services business needs banner showcasing past stock picks

We are looking for a banner for our Vancouver B.C. based company named 'BrightLedger Financial'. Our website is www.ledgerpicks-demo.com and we provide several stock picking services to clients which we let them know which stocks to buy. We have an impressive track record of picking some of the best stocks on the Canadian and American stock markets and we would like to showcase some of these stocks to prospective clients at conferences.

```html
<!DOCTYPE html>
<html lang="en">
<head>
<meta charset="utf-8">
<title>BrightLedger Financial – Roll-up Banner</title>
<link rel="stylesheet" href="https://fonts.googleapis.com/css2?family=Montserrat:wght@500&family=Rokkitt:wght@400;800&display=swap">
<style>
  :root {
    --page-bg: #e4e4e7;
    --teal: #23a99a;
    --navy: #2b3a4a;
    --white: #ffffff;
    --ink: #2b3a4a;
    --chart-line: #d2283c;
    --chart-grid: #dcdcdc;
    --chart-bg: #f3f3f3;
    --chart-text: #555555;
    --photo-dark: #3b2a20;
    --photo-mid: #7a5a40;
    --photo-light: #c9c3bb;
  }
  html, body {
    margin: 0;
    width: 1200px;
    height: 1200px;
    overflow: hidden;
    background: var(--page-bg);
  }
  .banner {
    position: absolute;
    left: 362px;
    top: 30px;
    width: 705px;
    height: 1688px;
    transform: scale(0.67536);
    transform-origin: 0 0;
    background: var(--white);
    overflow: hidden;
    font-family: "Rokkitt", Georgia, serif;
    box-shadow: 0 6px 24px rgba(0,0,0,0.12);
  }
  .banner-shapes, .hero-photo { position: absolute; left: 0; top: 0; }
  .brand {
    position: absolute;
    top: 40px;
    left: 0;
    width: 100%;
    text-align: center;
  }
  .brand-square {
    width: 66px;
    height: 66px;
    margin: 0 auto 28px;
    background: var(--teal);
  }
  .brand-name {
    margin: 0;
    font-weight: 400;
    font-size: 46px;
    letter-spacing: 1px;
    color: var(--teal);
    line-height: 1;
  }
  .brand-tagline {
    margin: 20px 0 0;
    font-family: "Montserrat", Arial, sans-serif;
    font-weight: 500;
    font-size: 21px;
    letter-spacing: 4.6px;
    color: var(--ink);
  }
  .pitch {
    position: absolute;
    top: 778px;
    left: 0;
    width: 100%;
    text-align: center;
    color: var(--white);
  }
  .pitch-headline {
    margin: 0;
    font-weight: 800;
    font-size: 40px;
    line-height: 1;
  }
  .pitch-sub {
    margin: 8px 0 0;
    font-size: 25px;
    line-height: 27px;
  }
  .services-title {
    margin: 30px 0 6px;
    font-weight: 800;
    font-size: 38px;
    line-height: 1;
  }
  .services-list {
    list-style: none;
    margin: 0;
    padding: 0;
    font-size: 28px;
    line-height: 27px;
  }
  .services-list li.dot { font-size: 26px; line-height: 27px; }
  .chart-card {
    position: absolute;
    width: 252px;
    height: 178px;
    background: var(--white);
    box-shadow: 0 3px 8px rgba(0,0,0,0.25);
  }
  .chart-card svg { display: block; }
  .chart-card.one { left: 89px; top: 1179px; }
  .chart-card.two { left: 358px; top: 1179px; }
  .chart-card.three { left: 225px; top: 1374px; }
  .cta {
    position: absolute;
    left: 99px;
    top: 1574px;
    width: 506px;
    height: 91px;
    border-radius: 10px;
    background: var(--navy);
    text-align: center;
  }
  .cta-line {
    margin: 10px 0 0;
    font-weight: 400;
    font-size: 34px;
    line-height: 1;
    color: var(--teal);
  }
  .cta-url {
    margin: 4px 0 0;
    font-size: 30px;
    line-height: 1;
    color: var(--white);
  }
</style>
</head>
<body>
<main class="banner">
  <svg class="banner-shapes" width="705" height="1688" viewBox="0 0 705 1688" aria-hidden="true">
    <path d="M0,262 C200,245 420,240 705,345 L705,1603 L0,1603 Z" fill="var(--teal)"/>
    <path d="M260,250 C450,226 600,255 705,300 L705,345 C560,292 420,262 260,250 Z" fill="var(--navy)"/>
  </svg>

  <svg class="hero-photo" width="705" height="763" viewBox="0 0 705 763" role="img" aria-label="Photo from above of an advisor at a wooden desk reviewing stock charts beside a laptop and a cup of coffee">
    <defs>
      <linearGradient id="photoTone" x1="0" y1="0" x2="1" y2="1">
        <stop offset="0" stop-color="var(--photo-mid)"/>
        <stop offset="0.45" stop-color="var(--photo-dark)"/>
        <stop offset="1" stop-color="var(--photo-light)"/>
      </linearGradient>
    </defs>
    <path d="M0,325 C200,300 420,295 705,372 L705,763 L0,763 Z" fill="url(#photoTone)"/>
  </svg>

  <header class="brand">
    <div class="brand-square"></div>
    <h1 class="brand-name">BRIGHTLEDGER FINANCIAL</h1>
    <p class="brand-tagline">INDEPENDENT EQUITY ADVISORS</p>
  </header>

  <section class="pitch">
    <h2 class="pitch-headline">Research. Results. Freedom.</h2>
    <p class="pitch-sub">Building simple, winning stock portfolios<br>to beat the market.</p>
    <h3 class="services-title">Services:</h3>
    <ul class="services-list">
      <li>Canadian Small-Cap Stock Research</li>
      <li class="dot">•</li>
      <li>Canadian Income/Dividend Stock Reseach</li>
      <li class="dot">•</li>
      <li>U.S. Growth/Value Stock Research</li>
      <li class="dot">•</li>
      <li>Simple TFSA</li>
    </ul>
  </section>

  <svg width="0" height="0" style="position:absolute" aria-hidden="true">
    <defs>
      <g id="chartFrame">
        <rect x="36" y="40" width="194" height="118" fill="var(--chart-bg)"/>
        <g stroke="var(--chart-grid)" stroke-width="0.6">
          <line x1="36" y1="64" x2="230" y2="64"/><line x1="36" y1="88" x2="230" y2="88"/>
          <line x1="36" y1="112" x2="230" y2="112"/><line x1="36" y1="136" x2="230" y2="136"/>
        </g>
        <line x1="36" y1="158" x2="230" y2="158" stroke="#999" stroke-width="0.6"/>
        <g font-family="Arial, sans-serif" font-size="5" fill="var(--chart-text)">
          <text x="14" y="66">+80%</text><text x="14" y="90">+60%</text><text x="14" y="114">+40%</text>
          <text x="14" y="138">+20%</text><text x="20" y="160">0%</text>
          <text x="40" y="169">Q1</text><text x="88" y="169">Q2</text><text x="136" y="169">Q3</text><text x="184" y="169">Q4</text>
        </g>
        <text x="228" y="24" text-anchor="end" font-family="Arial, sans-serif" font-size="5" font-weight="700" fill="var(--chart-text)">HARBOR DATA</text>
      </g>
    </defs>
  </svg>

  <div class="chart-card one">
    <svg width="252" height="178" viewBox="0 0 252 178" role="img" aria-label="Line chart of a past stock pick rising over one year">
      <text x="18" y="20" font-family="Arial, sans-serif" font-size="7" font-weight="700" fill="#333">Pick Tracker: Pick A</text>
      <text x="18" y="29" font-family="Arial, sans-serif" font-size="5" fill="#777">Gain since entry</text>
      <use href="#chartFrame"/>
      <polyline fill="none" stroke="var(--chart-line)" stroke-width="1.2"
        points="38,156 50,150 62,152 74,142 86,138 98,130 110,134 122,120 134,112 146,116 158,100 170,94 182,98 194,82 206,76 218,70 228,62"/>
    </svg>
  </div>
  <div class="chart-card two">
    <svg width="252" height="178" viewBox="0 0 252 178" role="img" aria-label="Line chart of a past stock pick climbing after a flat start">
      <text x="18" y="20" font-family="Arial, sans-serif" font-size="7" font-weight="700" fill="#333">Pick Tracker: Pick B</text>
      <text x="18" y="29" font-family="Arial, sans-serif" font-size="5" fill="#777">Gain since entry</text>
      <use href="#chartFrame"/>
      <polyline fill="none" stroke="var(--chart-line)" stroke-width="1.2"
        points="38,154 50,150 62,155 74,148 86,150 98,146 110,140 122,128 134,118 146,104 158,96 170,90 182,78 194,72 206,60 218,56 228,50"/>
    </svg>
  </div>
  <div class="chart-card three">
    <svg width="252" height="178" viewBox="0 0 252 178" role="img" aria-label="Line chart of a past stock pick with a steady upward trend">
      <text x="18" y="20" font-family="Arial, sans-serif" font-size="7" font-weight="700" fill="#333">Pick Tracker: Pick C</text>
      <text x="18" y="29" font-family="Arial, sans-serif" font-size="5" fill="#777">Gain since entry</text>
      <use href="#chartFrame"/>
      <polyline fill="none" stroke="var(--chart-line)" stroke-width="1.2"
        points="38,157 50,146 62,140 74,144 86,132 98,124 110,128 122,116 134,108 146,112 158,102 170,106 182,92 194,86 206,90 218,78 228,72"/>
    </svg>
  </div>

  <footer class="cta">
    <p class="cta-line">BECOME A CLIENT TODAY !</p>
    <p class="cta-url">www.ledgerpicks-demo.com</p>
  </footer>
</main>
</body>
</html>
```